Holiday Business Card for Tarvo Corporation

Need artwork for print production. Holiday card for clients. Do not want laser cutting or oversized postage costs. We are a geotechnical engineering company.

CEOs, engineers, geologists, developers (housing, retail, commercial), public agencies (Schools, roads, pipelines)

Professional Service

• use uploaded logo

```html
<!DOCTYPE html>
<html lang="en">
<head>
<meta charset="utf-8">
<title>Tarvo Corporation Holiday Card</title>
<link rel="stylesheet" href="https://fonts.googleapis.com/css2?family=Tinos:wght@700&family=Great+Vibes&family=Arimo:wght@400&display=swap">
<style>
  :root {
    --backdrop: #ececec;
    --card-navy: #222c63;
    --card-navy-light: #2a3570;
    --silver: #9c9c9c;
    --silver-text: #8e8e8e;
    --white: #ffffff;
  }
  * { margin: 0; padding: 0; box-sizing: border-box; }
  html, body {
    width: 1200px;
    height: 1000px;
    overflow: hidden;
    background: var(--backdrop);
  }
  .canvas {
    position: relative;
    width: 1200px;
    height: 1000px;
  }
  .holiday-card {
    position: absolute;
    left: 130px;
    top: 170px;
    width: 940px;
    height: 660px;
    background: var(--card-navy);
    overflow: hidden;
  }
  .star-pattern {
    position: absolute;
    inset: 0;
    background: radial-gradient(ellipse at center, var(--card-navy) 0%, var(--card-navy) 45%, var(--card-navy-light) 100%);
  }
  .greeting {
    position: absolute;
    left: 0;
    right: 0;
    top: 200px;
    text-align: center;
  }
  .greeting-thanks {
    font-family: "Tinos", "Times New Roman", serif;
    font-weight: 700;
    font-size: 52px;
    line-height: 1;
    color: var(--silver-text);
    letter-spacing: 1px;
  }
  .greeting-holidays {
    position: relative;
    margin-top: 2px;
    font-family: "Great Vibes", cursive;
    font-size: 92px;
    line-height: 1;
    color: var(--white);
  }
  .greeting-underline {
    display: block;
    margin: -14px auto 0;
    width: 540px;
    height: 30px;
  }
  .company-name {
    margin-top: 4px;
    font-family: "Arimo", Arial, sans-serif;
    font-size: 50px;
    line-height: 1;
    color: var(--silver-text);
  }
</style>
</head>
<body>
  <div class="canvas">
    <section class="holiday-card">
      <div class="star-pattern" role="img" aria-label="Scattered silver geometric star outlines and small white and grey dots across the navy card"></div>
      <div class="greeting">
        <p class="greeting-thanks">Thank You</p>
        <p class="greeting-holidays">Happy Holidays</p>
        <svg class="greeting-underline" viewBox="0 0 540 30" aria-hidden="true">
          <line x1="0" y1="26" x2="130" y2="20" stroke="#ffffff" stroke-width="3"/>
          <line x1="210" y1="17" x2="540" y2="2" stroke="#ffffff" stroke-width="3"/>
        </svg>
        <p class="company-name">Tarvo</p>
      </div>
    </section>
  </div>
</body>
</html>
```